Bravik Telecom Branding and Visual Identity Project

We need some visual identity items for Bravik Telecom, which should be produced based on the company's logo attached.

I would like the brochure to be as lightweight as possible so that it can be sent via email.

Below are the items we need to be made.

- Company letterhead
- Company brochure in PDF format (single page)
- Email signature (only one)
- Wallpaper
- Banner for use on social media
- Customized shirt

Target Market(s)

Passengers and crew members of ships

Industry/Entity Type

Telecom & Maritime

Colors
0054AA
0677BA
7BADD7
CADEEF
E8F1F8

Requirements
Nice to have
• Colors that match the logo
Should not have
• Colors that clash with the logo colors

```html
<!DOCTYPE html>
<html lang="en">
<head>
<meta charset="utf-8">
<title>Bravik Telecom Letterhead</title>
<link href="https://fonts.googleapis.com/css2?family=Arimo:wght@400&family=Mulish:wght@700;800&family=Open+Sans:wght@400&display=swap" rel="stylesheet">
<style>
  :root {
    --backdrop: #9a9a9a;
    --paper: #ffffff;
    --brand-blue: #0670b8;
    --band-grey: #b3b3b3;
    --rule-grey: #a8a8a8;
    --text-dark: #4d4d4d;
    --text-body: #555555;
    --text-contact: #7a7a7a;
  }
  html, body {
    margin: 0;
    padding: 0;
    width: 1033px;
    height: 1200px;
    overflow: hidden;
    background: var(--backdrop);
  }
  .letterhead {
    position: absolute;
    left: 174px;
    top: 116px;
    width: 685px;
    height: 969px;
    background: var(--paper);
    overflow: hidden;
  }
  .brand-name {
    position: absolute;
    left: 48px;
    top: 78px;
    margin: 0;
    font-family: "Mulish", sans-serif;
    font-weight: 800;
    font-size: 30px;
    line-height: 1;
    color: var(--brand-blue);
    letter-spacing: -0.2px;
  }
  .header-rule {
    position: absolute;
    left: 48px;
    top: 129px;
    width: 589px;
    height: 1px;
    background: var(--rule-grey);
  }
  .contact {
    position: absolute;
    left: 514px;
    top: 49px;
    font-family: "Arimo", sans-serif;
    font-size: 11px;
    color: var(--text-contact);
    line-height: 13px;
  }
  .contact-address { margin: 0 0 6px; }
  .contact-list { list-style: none; margin: 0; padding: 0; }
  .contact-list li { display: flex; align-items: center; height: 13px; }
  .contact-icon { width: 8px; height: 8px; margin-right: 7px; flex: none; }
  .salutation {
    position: absolute;
    left: 63px;
    top: 296px;
    margin: 0;
    font-family: "Mulish", sans-serif;
    font-weight: 700;
    font-size: 16px;
    color: var(--text-dark);
  }
  .letter-body {
    position: absolute;
    left: 61px;
    top: 343px;
    width: 565px;
    font-family: "Arimo", sans-serif;
    font-size: 11.6px;
    line-height: 14px;
    color: var(--text-body);
  }
  .letter-body p { margin: 0 0 12px; }
  .closing {
    position: absolute;
    left: 63px;
    top: 629px;
    margin: 0;
    font-family: "Mulish", sans-serif;
    font-weight: 700;
    font-size: 9px;
    color: var(--text-dark);
  }
  .signature {
    position: absolute;
    left: 79px;
    top: 677px;
    margin: 0;
    font-family: "Open Sans", sans-serif;
    font-size: 17px;
    letter-spacing: -1px;
    color: var(--text-dark);
  }
  .footer-band {
    position: absolute;
    left: 0;
    bottom: 0;
    width: 685px;
    height: 13px;
  }
</style>
</head>
<body>
  <main class="letterhead">
    <h1 class="brand-name">Bravik Telecom</h1>
    <div class="header-rule"></div>

    <address class="contact">
      <p class="contact-address">Your address, city<br>state, ZIP 0000</p>
      <ul class="contact-list">
        <li>
          <svg class="contact-icon" viewBox="0 0 10 10" aria-hidden="true">
            <circle cx="5" cy="5" r="5" fill="var(--brand-blue)"/>
            <path d="M3 2.4 L4.1 2.2 L4.6 3.6 L3.9 4.1 Q4.6 5.5 5.9 6.1 L6.4 5.4 L7.8 5.9 L7.6 7 Q4 7.4 3 2.4Z" fill="#fff"/>
          </svg>
          123-456-2100
        </li>
        <li>
          <svg class="contact-icon" viewBox="0 0 10 10" aria-hidden="true">
            <rect x="0.5" y="2" width="9" height="6.5" fill="var(--brand-blue)"/>
            <path d="M0.8 2.4 L5 5.6 L9.2 2.4" stroke="#fff" stroke-width="0.9" fill="none"/>
          </svg>
          youremail@mailbox.com
        </li>
        <li>
          <svg class="contact-icon" viewBox="0 0 10 10" aria-hidden="true">
            <circle cx="5" cy="5" r="5" fill="var(--brand-blue)"/>
            <ellipse cx="5" cy="5" rx="2" ry="4.2" stroke="#fff" stroke-width="0.8" fill="none"/>
            <path d="M1 5 H9" stroke="#fff" stroke-width="0.8"/>
          </svg>
          www.yourwebsite.com
        </li>
      </ul>
    </address>

    <h2 class="salutation">Dear Mr. Smith,</h2>

    <section class="letter-body">
      <p>Lorem ipsum dolor sit amet, consectetuer adipiscing elit, sed diam nonmmy nibh euismod tincidunt ut laor eet dolore magna aliquam erat volutpat. Ut wisi enim ad minim veniam, quis nostrud exerci tationmcorper suscipit lobortis nisl ut aliquip ex ea commodo consequat. Duis autem vel eum iriure dolor in hendrerit in vulputate velit esse molestie consequat, vel illum dolore eu feugiat</p>
      <p>Rorem ipsum dolor sit amet, consectetuer adipiscing elit, sed diam nonmmy nibh euismod tincidunt ut laor eet dolore magna aliquam erat volutpat. Ut wisi enim ad minim veniam, quis nostrud exerci tationmcorper suscipit lobortis nisl ut aliquip ex ea commodo consequat. Duis autem vel eum iriure dolor in hendrerit in vulputate velit esse molest</p>
      <p>Dorem ipsum dolor sit amet, consectetuer adipiscing elit, sed diam nonmmy nibh euismod tincidunt ut laor eet dolore magna aliquam erat volutpat. Ut wisi enim ad minim veniam, quis nostrud exerci tationmcorper suscipit lobortis nisl ut aliquip ex ea commodo consequat. Duis autem vel eum iriure dolor in hendrerit in suscipit lobortis nisl ut aliquip ex ea commodo consequat. Duis autem vel eum iriure dolor in hendrerit in vulputate velit esse molestie consequat, vel illum</p>
      <p>Sorem ipsum dolor sit amet, consectetuer adipiscing elit, sed diam nonmmy nibh euismod tincidunt ut laor eet dolore magna aliquam erat volutpat. Ut wisi enim ad minim veniam, quis nostrud exerci tationmcorper suscipit lobortis nisl ut aliquip ex ea commodo consequat. Duis autem vel eum iriure dolor in</p>
    </section>

    <p class="closing">Sincerely,</p>
    <p class="signature">Marten Olsby</p>

    <svg class="footer-band" viewBox="0 0 685 13" preserveAspectRatio="none" aria-hidden="true">
      <polygon points="0,0 523,0 510,13 0,13" fill="var(--brand-blue)"/>
      <polygon points="532,0 685,0 685,13 519,13" fill="var(--band-grey)"/>
    </svg>
  </main>
</body>
</html>
```